Business Card and Letterhead for new HR Consultancy

A business card and letterhead design that includes the logo (attached in jpg) and the business tag line which is "Building on Your Best Resource"
We are based in regional New South Wales, Australia and provide HR services to small and medium business owners to support them grow their businesses by focusing on their people. The services provided cover the full range of HR management from simple advice through to comprehensive programs that support people management. My clients typically will not have a HR manager, either because they don't need to employ one or can't afford to hire one. So they will be looking for me to provide good services, add value to their business for a competitive price.
I am a middle aged woman with over 15 years expertise in all facets of HR Management. My clients need to know they can trust me, that I am credible and competent and open in my relationship with them and that I can make a positive difference for them.
I would like to see designs that are modern and communicate value for money.
Updates
A note to advise that the email address is
xxxxxxx@willowbankstaff.com.au
website will be
www.willowbankstaff.com.au
thanks
M.
Will also need to include the business number (indicates it is a registered business).
ABN: 37 218 405 963
Target Market(s)
small to medium sized business owners 30 years and over, professional and tradespeople
Industry/Entity Type
Business
Look and feel

```html
<!DOCTYPE html>
<html lang="en">
<head>
<meta charset="utf-8">
<title>Willowbank – Business Cards</title>
<link rel="stylesheet" href="https://fonts.googleapis.com/css2?family=Ubuntu:wght@400;500;700&display=swap">
<style>
  :root {
    --canvas-bg: #e7ebec;
    --card-bg: #ffffff;
    --band-green: #159a26;
    --brand-green: #1c9a2c;
    --text-brown: #6e5a4c;
    --accent-red: #d8363f;
  }
  * { box-sizing: border-box; margin: 0; padding: 0; }
  html, body {
    width: 1200px;
    height: 960px;
    overflow: hidden;
    background: var(--canvas-bg);
    font-family: "Ubuntu", sans-serif;
  }
  .sheet {
    width: 1200px;
    height: 960px;
    display: flex;
    flex-direction: column;
    align-items: center;
    justify-content: center;
    gap: 40px;
  }
  .card {
    position: relative;
    width: 700px;
    height: 400px;
    background: var(--card-bg);
    border-top: 12px solid var(--band-green);
    border-bottom: 24px solid var(--band-green);
    box-shadow: 0 6px 18px rgba(40, 60, 70, 0.18);
  }

  /* Contact side */
  .card--contact { display: flex; }
  .brand-block {
    width: 300px;
    display: flex;
    align-items: center;
    justify-content: center;
    gap: 10px;
  }
  .brand-dot {
    width: 18px;
    height: 18px;
    border-radius: 50%;
    background: var(--accent-red);
  }
  .brand-name {
    font-weight: 700;
    font-size: 36px;
    color: var(--brand-green);
  }
  .contact-block {
    padding: 58px 0 0 40px;
    color: var(--text-brown);
  }
  .person {
    font-size: 27px;
    font-weight: 500;
    margin-bottom: 28px;
  }
  .person .role {
    font-size: 16px;
    font-weight: 400;
    text-transform: uppercase;
    letter-spacing: 0.5px;
  }
  .contact-group {
    font-size: 16px;
    line-height: 1.4;
    margin-bottom: 24px;
  }
  .contact-group .web-accent { color: var(--brand-green); }

  /* Brand side */
  .card--brand {
    display: flex;
    flex-direction: column;
    align-items: center;
  }
  .brand-lockup {
    margin-top: 120px;
    display: flex;
    align-items: center;
    gap: 16px;
  }
  .brand-lockup .brand-dot { width: 24px; height: 24px; }
  .brand-lockup .brand-name { font-size: 56px; }
  .tagline {
    margin-top: auto;
    margin-bottom: 16px;
    font-size: 19px;
    font-weight: 500;
    letter-spacing: 0.6px;
    color: var(--brand-green);
  }
</style>
</head>
<body>
<main class="sheet">
  <section class="card card--contact" aria-label="Business card, contact side">
    <div class="brand-block">
      <span class="brand-dot"></span>
      <span class="brand-name">Willowbank</span>
    </div>
    <div class="contact-block">
      <p class="person">Clare Hollis <span class="role">| Manager</span></p>
      <p class="contact-group">P.O. Box 412<br>Orange, NSW 2800</p>
      <p class="contact-group">t: 02 5550 1824<br>f: 02 5550 1825</p>
      <p class="contact-group">xxxxxxx@willowbankstaff.com.au<br>www.<span class="web-accent">willowbankstaff</span>.com.au</p>
    </div>
  </section>

  <section class="card card--brand" aria-label="Business card, brand side">
    <div class="brand-lockup">
      <span class="brand-dot"></span>
      <span class="brand-name">Willowbank</span>
    </div>
    <p class="tagline">Building on Your Best Resource</p>
  </section>
</main>
</body>
</html>
```